Financial Services Consultant needs a business card

We need a business card for a new consulting company based in Melbourne called
"Korvane Metrics". Tagline is TRACK, REVIEW, GROW
We would like to see business card designs that are in line with the minimal style of the website www.korvane-metrics-example.com
The font I have used on the website is Proxima Nova and would like the same or similar font used on the business card with a minimal design in line with the website Two sided with "KORVANE METRICS" TRACK, REVIEW, GROW on one side and name, title and contact details on the otther
Updates

Hi All, thanks for your submissions, much appreciated.

I have recently added some colour to my webiste, it is hex #3a7b74 for those that wish to use it
Thanks

Hi all

thanks very much for your design submissions I am very impressed and they are much appreciated.

Interms of general feedback please find below;

Colour: I am trying to stick to a minimal design and colour scheme for my website which is still under construction, up to 3 colours( www.korvane-metrics-example.com) it is currently black and white with a small amount of blue/green but I am open to suggestion/interpretations for a consulting company.

Card: I dont mind if it has rounded edges or straight, I was thinking about using a letterpress card if possible

Detail: the detail on the card will include; Name, Title, Mobile, Personal Email, Business Email,Web,Business Address

Once again thanks for submissions

Industry/Entity Type

Business

```html
<!DOCTYPE html>
<html lang="en">
<head>
<meta charset="utf-8">
<title>Korvane Metrics — Business Card</title>
<link rel="stylesheet" href="https://fonts.googleapis.com/css2?family=Figtree:wght@400;500;600&display=swap">
<style>
  :root {
    --backdrop: #232323;
    --paper: #f4f4f4;
    --ink: #333333;
    --ink-soft: #444444;
    --teal: #6aaea2;
    --teal-deep: #5e9e92;
    --teal-emboss: #579488;
    --teal-text: #77b9ad;
    --faint-mark: #e0e0e0;
    --tagline: #2e4743;
  }
  * { margin: 0; padding: 0; box-sizing: border-box; }
  html, body {
    width: 1200px; height: 900px; overflow: hidden;
    background: var(--backdrop);
    font-family: "Figtree", "Helvetica Neue", Arial, sans-serif;
  }
  .stage { position: relative; width: 1200px; height: 900px; }

  .card {
    position: absolute; left: 354px; width: 488px; height: 278px;
    overflow: hidden;
  }
  .card--front { top: 154px; background: var(--paper); }
  .card--back {
    top: 463px;
    background: linear-gradient(180deg, var(--teal) 0%, var(--teal-deep) 100%);
  }

  .side-mark {
    position: absolute; left: 32px; top: 262px; width: 246px;
    transform: rotate(-90deg); transform-origin: 0 0;
    font-size: 21px; font-weight: 600; letter-spacing: 2.4px;
    line-height: 24px;
    color: var(--faint-mark); white-space: nowrap;
  }

  .identity {
    position: absolute; right: 32px; top: 36px; text-align: right;
  }
  .identity__name { font-size: 23px; font-weight: 500; color: var(--ink); line-height: 1.1; }
  .identity__title { font-size: 15px; letter-spacing: 0.8px; color: var(--teal-text); margin-top: 2px; }

  .address {
    position: absolute; right: 32px; top: 120px; text-align: right;
    font-style: normal;
    font-size: 13.5px; line-height: 17px; color: var(--ink-soft);
  }
  .address__company { font-weight: 600; color: var(--ink); }

  .contact {
    position: absolute; left: 205px; top: 180px; width: 266px; height: 82px;
    background: var(--teal); color: #f2f8f6;
    padding: 17px 14px 0 0;
    font-size: 12.5px; line-height: 16px;
  }
  .contact__row { display: flex; justify-content: flex-end; white-space: nowrap; }
  .contact__label { width: 22px; display: flex; justify-content: space-between; padding-left: 5px; }

  .brand {
    position: absolute; left: 0; right: 0; top: 117px; text-align: center;
    font-size: 34px; font-weight: 400; letter-spacing: 4px;
    color: var(--teal-emboss);
  }
  .tagline {
    position: absolute; left: 0; right: 0; top: 178px; text-align: center;
    font-size: 14px; letter-spacing: 4px; color: var(--tagline);
  }
</style>
</head>
<body>
<main class="stage">
  <section class="card card--front" aria-label="Business card front">
    <div class="side-mark">KORVANE METRICS</div>
    <div class="identity">
      <p class="identity__name">Elena Marsh</p>
      <p class="identity__title">PRESIDENT</p>
    </div>
    <address class="address">
      <p class="address__company">Korvane Metrics PTY LTD.</p>
      <p>Alder Lane, #12</p>
      <p>Melbourne, 3000, Victoria</p>
    </address>
    <div class="contact">
      <p class="contact__row"><span>03 555-010-2468</span><span class="contact__label"><span>:</span><span>t</span></span></p>
      <p class="contact__row"><span>elena@korvane-metrics-example.com</span><span class="contact__label"><span>:</span><span>e</span></span></p>
      <p class="contact__row"><span>www.korvane-metrics-example.com</span><span class="contact__label"><span>:</span><span>w</span></span></p>
    </div>
  </section>

  <section class="card card--back" aria-label="Business card back">
    <p class="brand">KORVANE METRICS</p>
    <p class="tagline">TRACK, REVIEW, GROW</p>
  </section>
</main>
</body>
</html>
```